New Web Design Project

See attachments on the content and concept. Very important that the flow of the tiers stand out

Target Market(s)

Food and Beverage Manufacturing

Industry/Entity Type

Food and Beverage

Coding

Coded - Design and coding required

Number of Pages Required

3 page

Colors
0054AA
0677BA
7BADD7
CADEEF
E8F1F8

```html
<!DOCTYPE html>
<html lang="en">
<head>
<meta charset="utf-8">
<title>Northline Food Safety Group — SQF Consulting</title>
<link href="https://fonts.googleapis.com/css2?family=Lexend:wght@300;400;500;600;700&display=swap" rel="stylesheet">
<style>
:root{
  --navy:#0a3f8a;
  --blue:#0054AA;
  --mid:#0677BA;
  --sky:#7BADD7;
  --pale:#CADEEF;
  --mist:#E8F1F8;
  --ink:#1b2433;
  --muted:#4a5566;
  --white:#ffffff;
}
*{box-sizing:border-box;margin:0;padding:0}
html,body{width:1200px;height:4605px;overflow:hidden}
body{font-family:"Lexend",sans-serif;color:var(--ink);background:var(--white);position:relative}
a{text-decoration:none;color:inherit}
.abs{position:absolute}

/* header */
.site-header{position:absolute;top:0;left:0;width:1200px;height:75px;display:flex;align-items:center;padding:0 93px;background:#fff}
.brand{display:flex;align-items:center;gap:12px}
.brand-mark{width:44px;height:44px;border:3px solid var(--blue);border-radius:50%}
.brand-name{font-weight:600;font-size:17px;color:var(--blue);line-height:1.1}
.brand-sub{font-size:11px;color:var(--mid);font-weight:400}
.main-nav{display:flex;gap:46px;margin-left:auto;margin-right:46px;font-size:12px;font-weight:500;letter-spacing:.04em;color:var(--ink)}
.btn-nav{background:var(--blue);color:#fff;font-size:11px;font-weight:600;border-radius:24px;padding:12px 14px 12px 26px;display:flex;align-items:center;gap:12px}
.btn-nav span{width:24px;height:24px;border-radius:50%;background:#fff;color:var(--blue);display:flex;align-items:center;justify-content:center;font-size:13px}

/* hero */
.hero{position:absolute;top:75px;left:0;width:1200px;height:617px;overflow:hidden;background:var(--blue)}
.hero-photo{position:absolute;top:0;right:0;width:780px;height:617px;background:linear-gradient(135deg,#c9d6e2,#e7edf2 40%,#aab9c8);clip-path:polygon(22% 0,100% 0,100% 100%,48% 100%)}
.hero-shade{position:absolute;top:0;left:0;width:1200px;height:617px;background:linear-gradient(90deg,#0d4ea0 0%,#0054AA 38%,rgba(0,84,170,0) 60%)}
.hero-copy{position:absolute;left:95px;top:143px;width:520px;color:#fff}
.eyebrow-light{font-size:13px;letter-spacing:.04em;margin-bottom:14px}
.hero h1{font-size:34px;font-weight:500;line-height:1.2;margin-bottom:18px}
.hero p{font-size:13.5px;line-height:1.45;font-weight:300;margin-bottom:26px;max-width:420px}
.hero-actions{display:flex;gap:14px}
.btn-white{background:#fff;color:var(--blue);font-weight:600;font-size:13px;border-radius:26px;padding:14px 24px}
.btn-ghost{border:2px solid #fff;color:#fff;font-weight:500;font-size:13px;border-radius:26px;padding:12px 40px}

/* stats */
.stats{position:absolute;top:692px;left:0;width:1200px;height:126px;display:flex;justify-content:space-around;align-items:center;padding:0 60px;border-bottom:1px solid var(--pale)}
.stat{text-align:center;color:var(--blue)}
.stat-num{font-size:38px;font-weight:600;line-height:1.1}
.stat-label{font-size:14px;font-weight:500;margin-top:8px}
.stat svg{display:block;margin:0 auto}

/* section heads */
.sec-head{text-align:center}
.sec-icon{display:block;margin:0 auto 10px}
.sec-eyebrow{font-size:15px;color:var(--mid);letter-spacing:.03em;margin-bottom:12px}
.sec-title{font-size:36px;font-weight:500;line-height:1.22;color:var(--ink)}
.sec-title em{font-style:normal;color:var(--blue)}
.sec-lead{font-size:16px;color:var(--ink);line-height:1.45;font-weight:300;margin-top:22px}

/* services */
.services{position:absolute;top:818px;left:0;width:1200px;height:972px}
.services .sec-head{position:absolute;top:48px;left:0;width:1200px}
.card-grid{position:absolute;top:240px;left:93px;width:1042px;display:grid;grid-template-columns:repeat(3,329px);gap:28px 27px}
.svc-card{height:304px;border:1px solid var(--pale);border-radius:6px;box-shadow:0 4px 14px rgba(0,84,170,.08);text-align:center;padding:32px 34px;background:#fff}
.svc-card.featured{background:linear-gradient(160deg,#0054AA,#0a3f8a);color:#fff;border-color:var(--blue)}
.svc-ico{width:74px;height:74px;border:1px solid var(--pale);border-radius:6px;margin:0 auto 24px;display:flex;align-items:center;justify-content:center;background:#fff}
.svc-card h3{font-size:18px;font-weight:500;margin-bottom:10px}
.svc-card p{font-size:12.5px;line-height:1.6;color:var(--muted);font-weight:300}
.svc-card.featured p{color:#e4eefa}

/* why */
.why{position:absolute;top:1790px;left:0;width:1200px;height:905px;background:var(--mist)}
.why .sec-head{position:absolute;top:42px;left:0;width:1200px}
.hex-frame{position:absolute;left:63px;top:365px}
.benefits{position:absolute;left:605px;top:353px;width:545px}
.benefit{display:flex;gap:20px;margin-bottom:34px}
.benefit-ico{flex:0 0 72px;height:66px;border-radius:4px;background:#fff;display:flex;align-items:center;justify-content:center}
.benefit-ico.on{background:var(--blue)}
.benefit h4{font-size:17px;font-weight:500;margin:2px 0 8px}
.benefit p{font-size:11px;line-height:1.5;color:var(--muted);font-weight:300}

/* process */
.process{position:absolute;top:2695px;left:0;width:1200px;height:645px}
.process .sec-head{position:absolute;top:36px;left:0;width:1200px}
.steps{position:absolute;top:232px;left:120px;width:960px;display:grid;grid-template-columns:repeat(4,240px)}
.step{text-align:center;padding:0 16px}
.step svg{display:block;margin:0 auto 22px}
.step h3{font-size:18px;font-weight:500;margin-bottom:10px}
.step p{font-size:11.5px;line-height:1.45;color:var(--muted);font-weight:300}

/* testimonial */
.quote{position:absolute;top:3340px;left:93px;width:1022px;height:345px;border-radius:8px;background:linear-gradient(180deg,#e3edf7,#d6e5f3);text-align:center;padding-top:64px}
.quote-mark{font-size:90px;line-height:.6;color:var(--blue);font-weight:700;height:48px}
.quote blockquote{font-size:21px;line-height:1.33;color:var(--navy);max-width:760px;margin:20px auto 26px;font-weight:400}
.quote cite{font-style:normal;font-size:15px;font-weight:500;color:var(--navy)}

/* credentials */
.creds{position:absolute;top:3735px;left:140px;width:920px;display:flex;justify-content:space-between;align-items:center}
.cred{display:flex;align-items:center;gap:12px;font-size:16px;font-weight:500}
.sigma{font-size:32px;color:var(--blue);font-weight:300}

/* cta */
.cta{position:absolute;top:3815px;left:0;width:1200px;height:443px;background:linear-gradient(180deg,#0054AA,#0a4d9c);color:#fff;text-align:center;padding-top:74px}
.cta .sec-eyebrow{color:#fff;font-size:16px}
.cta h2{font-size:46px;font-weight:500;margin:4px 0 20px}
.cta p{font-size:16px;line-height:1.55;font-weight:300}
.cta-actions{display:flex;justify-content:center;gap:16px;margin-top:36px}
.cta .btn-white{padding:13px 48px}
.cta .btn-ghost{padding:11px 26px;font-size:13px}

/* footer */
.site-footer{position:absolute;top:4258px;left:0;width:1200px;height:347px;background:#fff}
.foot-brand{position:absolute;left:155px;top:64px;width:360px}
.foot-brand p{font-size:13px;line-height:1.5;color:var(--navy);margin-top:30px;font-weight:300}
.foot-col{position:absolute;top:60px}
.foot-col h5{font-size:20px;font-weight:500;color:var(--blue);margin-bottom:16px}
.foot-col li{list-style:none;font-size:13px;color:var(--navy);margin-bottom:10px}
.foot-col li::before{content:"» ";color:var(--sky)}
.contact li::before{content:none}
.contact li{display:flex;align-items:center;gap:12px}
.dot{width:22px;height:22px;border-radius:50%;background:var(--blue);display:inline-block}
.copyright{position:absolute;left:93px;top:302px;width:1014px;border-top:1px solid var(--pale);padding-top:22px;text-align:center;font-size:12px;color:var(--muted)}
</style>
</head>
<body>

<header class="site-header">
  <div class="brand">
    <span class="brand-mark"></span>
    <div><div class="brand-name">Northline Food Safety Group</div><div class="brand-sub">Food Safety &amp; SQF Certification</div></div>
  </div>
  <nav class="main-nav"><a href="#">SERVICES</a><a href="#">BENEFITS</a><a href="#">PROCESS</a><a href="#">CONTACT</a></nav>
  <a class="btn-nav" href="#">GET SQF CONSULTATION <span>↗</span></a>
</header>

<section class="hero">
  <div class="hero-photo" role="img" aria-label="Food production line with workers in hairnets and lab coats inspecting products"></div>
  <div class="hero-shade"></div>
  <div class="hero-copy">
    <div class="eyebrow-light">SQF ONLY · TECH DRIVEN</div>
    <h1>Hire a Tech-driven SQF team that carries you across the certification finish line</h1>
    <p>At Northline Food Safety Group, we focus exclusively on SQF — combining real plant experience with smart technology so your team can stay focused on production while we handle the path to certification and beyond.</p>
    <div class="hero-actions"><a class="btn-white" href="#">Get SQF Consultation ↗</a><a class="btn-ghost" href="#">Explore Services ↗</a></div>
  </div>
</section>

<section class="stats">
  <div class="stat"><div class="stat-num">15+</div><div class="stat-label">Clients Onboarded</div></div>
  <div class="stat"><div class="stat-num">100%</div><div class="stat-label">100% SQF Focused</div></div>
  <div class="stat"><svg width="54" height="46" viewBox="0 0 54 46" fill="none" stroke="#0054AA" stroke-width="2"><rect x="18" y="14" width="18" height="14"/><circle cx="10" cy="8" r="5"/><circle cx="44" cy="8" r="5"/><circle cx="10" cy="36" r="5"/><circle cx="44" cy="36" r="5"/><path d="M15 10l5 5M39 10l-5 5M15 34l5-5M39 34l-5-5"/></svg><div class="stat-label">Digital Platform Built Programs</div></div>
  <div class="stat"><svg width="56" height="40" viewBox="0 0 56 40" fill="none" stroke="#0054AA" stroke-width="2"><path d="M4 8h46l2 10-6 10-10 2-6 8-6-6H10L4 20z"/></svg><div class="stat-label">US Nationwide Coverage</div></div>
</section>

<section class="services">
  <div class="sec-head">
    <svg class="sec-icon" width="30" height="32" viewBox="0 0 30 32" fill="none" stroke="#0054AA" stroke-width="2"><path d="M15 2l12 5v9c0 8-6 13-12 14C9 29 3 24 3 16V7z"/><path d="M10 16l4 4 7-8"/></svg>
    <div class="sec-eyebrow">WHAT WE DO</div>
    <h2 class="sec-title">SQF Consulting, Implementation<br><em>&amp; Onboarding</em></h2>
  </div>
  <div class="card-grid">
    <article class="svc-card"><div class="svc-ico"><svg width="34" height="34" viewBox="0 0 34 34" fill="none" stroke="#0054AA" stroke-width="2"><rect x="4" y="3" width="26" height="28"/><path d="M9 10h16M9 17h16M9 24h10"/></svg></div><h3>SQF Program Design</h3><p>We design your complete SQF system from scratch — HACCP/food safety plans, prerequisite programs, SOPs, forms, logs, and all required documentation tailored to your facility.</p></article>
    <article class="svc-card featured"><div class="svc-ico"><svg width="34" height="34" viewBox="0 0 34 34" fill="none" stroke="#0054AA" stroke-width="2"><rect x="9" y="9" width="16" height="16"/><path d="M13 3v6M21 3v6M13 25v6M21 25v6M3 13h6M3 21h6M25 13h6M25 21h6"/></svg></div><h3>Digital Platform Build</h3><p>We build your SQF program directly into modern food safety software like PlantLedger.io or SafeBatch.io — digitizing forms, checklists, monitoring logs, and workflows so your team runs paperless.</p></article>
    <article class="svc-card"><div class="svc-ico"><svg width="34" height="34" viewBox="0 0 34 34" fill="none" stroke="#0054AA" stroke-width="2"><circle cx="17" cy="10" r="5"/><circle cx="7" cy="18" r="4"/><circle cx="27" cy="18" r="4"/><path d="M8 32c0-6 4-10 9-10s9 4 9 10"/></svg></div><h3>Coaching &amp; Support</h3><p>After building your system, we coach your team to own and maintain it day-to-day. You run the program; we provide ongoing expert guidance so you stay audit-ready at all times.</p></article>
    <article class="svc-card"><div class="svc-ico"><svg width="34" height="34" viewBox="0 0 34 34" fill="none" stroke="#0054AA" stroke-width="2"><path d="M4 30V20M10 30V14M16 30V18"/><circle cx="24" cy="16" r="6"/><path d="M28 20l4 5"/></svg></div><h3>Gap Assessments</h3><p>We evaluate where your facility stands against SQF requirements, identify gaps, and provide a clear roadmap to close them before your audit — no surprises on certification day.</p></article>
    <article class="svc-card"><div class="svc-ico"><svg width="34" height="34" viewBox="0 0 34 34" fill="none" stroke="#0054AA" stroke-width="2"><circle cx="12" cy="12" r="5"/><circle cx="23" cy="12" r="5"/><path d="M4 28c0-5 4-8 8-8s8 3 8 8M15 28c0-5 4-8 8-8s7 3 7 8"/></svg></div><h3>Bilingual Team Support</h3><p>Our team in Central America supports Spanish-speaking employees within your operation — delivering training, documentation, and coaching in the language your floor team actually speaks.</p></article>
    <article class="svc-card"><div class="svc-ico"><svg width="34" height="34" viewBox="0 0 34 34" fill="none" stroke="#0054AA" stroke-width="2"><rect x="6" y="3" width="20" height="28"/><path d="M11 10h10M11 16h10"/><circle cx="24" cy="25" r="5"/><path d="M21.5 25l2 2 3-4"/></svg></div><h3>Sanitation &amp; Regulatory</h3><p>From sanitation program design to environmental monitoring, we help you build internal capabilities that meet USDA, FDA, and FSMA requirements and reduce dependence on external contractors.</p></article>
  </div>
</section>

<section class="why">
  <div class="sec-head">
    <svg class="sec-icon" width="30" height="32" viewBox="0 0 30 32" fill="none" stroke="#0054AA" stroke-width="2"><path d="M15 2l12 5v9c0 8-6 13-12 14C9 29 3 24 3 16V7z"/><path d="M10 16l4 4 7-8"/></svg>
    <div class="sec-eyebrow">WHY NORTHLINE FOOD SAFETY</div>
    <h2 class="sec-title">Built for Small &amp; Mid-Size<br><em>Manufacturers</em></h2>
    <p class="sec-lead">You don't need to hire a full-time food safety director or figure out SQF alone. We bring the<br>expertise and technology — you stay focused on production.<br>Consultant reviewing digital food safety compliance system in a manufacturing facility.</p>
  </div>
  <svg class="hex-frame" width="530" height="460" viewBox="0 0 530 460">
    <defs><linearGradient id="hexFill" x1="0" y1="0" x2="1" y2="1"><stop offset="0" stop-color="#dfe7ee"/><stop offset=".6" stop-color="#b9c8d6"/><stop offset="1" stop-color="#8ea4b8"/></linearGradient></defs>
    <polygon points="133,4 397,4 528,230 397,456 133,456 2,230" fill="none" stroke="#7BADD7" stroke-width="2"/>
    <polygon points="146,24 384,24 504,230 384,436 146,436 26,230" fill="url(#hexFill)" role="img" aria-label="Consultant using a tablet with a food safety compliance checklist in a production facility"/>
  </svg>
  <div class="benefits">
    <div class="benefit"><div class="benefit-ico on"><svg width="32" height="32" viewBox="0 0 32 32" fill="none" stroke="#fff" stroke-width="2"><circle cx="16" cy="13" r="9"/><path d="M11 21l-3 9 8-4 8 4-3-9"/><path d="M16 8v10M13 11h5"/></svg></div><div><h4>Lower Cost Than a Full-Time Hire</h4><p>Get a complete SQF team — program design, digital implementation, and coaching — at a fraction of the cost of hiring a full-time SQF Practitioner.</p></div></div>
    <div class="benefit"><div class="benefit-ico"><svg width="32" height="32" viewBox="0 0 32 32" fill="none" stroke="#0054AA" stroke-width="2"><path d="M4 12l12-6 12 6-12 6z"/><path d="M4 18l12 6 12-6M4 24l12 6 12-6"/></svg></div><div><h4>Your Program Lives in Software</h4><p>No more binders and spreadsheets. Your SQF system is built into PlantLedger.io or SafeBatch.io — organized, accessible, and always audit-ready.</p></div></div>
    <div class="benefit"><div class="benefit-ico"><svg width="32" height="32" viewBox="0 0 32 32" fill="none" stroke="#0054AA" stroke-width="2"><path d="M3 22h6l6 4 12-6-2-3-9 3"/><circle cx="20" cy="9" r="6"/></svg></div><div><h4>You Own It, We Support It</h4><p>We build the system and train your team. You maintain and run it day-to-day. We stay on call with coaching and advisory so you never feel stuck.</p></div></div>
    <div class="benefit"><div class="benefit-ico"><svg width="32" height="32" viewBox="0 0 32 32" fill="none" stroke="#0054AA" stroke-width="2"><circle cx="16" cy="16" r="6"/><path d="M16 3v6M16 23v6M3 16h6M23 16h6M7 7l4 4M21 21l4 4M25 7l-4 4M7 25l4-4"/></svg></div><div><h4>Flexible, Low-Risk Engagement</h4><p>Start with a 3-month commitment, then go month-to-month. Cancel anytime with 30 days notice. We earn your business every month.</p></div></div>
    <div class="benefit"><div class="benefit-ico"><svg width="32" height="32" viewBox="0 0 32 32" fill="none" stroke="#0054AA" stroke-width="2"><rect x="3" y="5" width="26" height="18"/><path d="M10 29h12M16 23v6"/><circle cx="11" cy="13" r="3"/><path d="M18 11h7M18 16h7"/></svg></div><div><h4>Bilingual Floor-Level Support</h4><p>With our Central America team, we provide training and documentation in Spanish so every member of your production team understands and follows the program.</p></div></div>
  </div>
</section>

<section class="process">
  <div class="sec-head">
    <svg class="sec-icon" width="30" height="32" viewBox="0 0 30 32" fill="none" stroke="#0054AA" stroke-width="2"><path d="M15 2l12 5v9c0 8-6 13-12 14C9 29 3 24 3 16V7z"/><path d="M10 16l4 4 7-8"/></svg>
    <div class="sec-eyebrow">HOW IT WORKS</div>
    <h2 class="sec-title">From Discovery to <em>Certification</em></h2>
    <p class="sec-lead" style="margin-top:16px">A clear, structured path that takes the guesswork out of SQF.</p>
  </div>
  <div class="steps">
    <div class="step">
      <svg width="190" height="190" viewBox="0 0 190 190"><circle cx="95" cy="95" r="88" fill="none" stroke="#0054AA" stroke-width="3" stroke-dasharray="330 6 2 6 2 6 2 6 2 6 2 6"/><circle cx="95" cy="95" r="72" fill="#0054AA"/><circle cx="95" cy="95" r="55" fill="#fff"/><path d="M78 74l10-4 6 12-6 5c3 7 8 12 15 15l5-6 12 6-4 10c-20 0-38-18-38-38z" fill="none" stroke="#0054AA" stroke-width="3"/><circle cx="27" cy="150" r="13" fill="#fff" stroke="#7BADD7" stroke-width="2"/><text x="27" y="155" text-anchor="middle" font-family="Lexend,sans-serif" font-size="14" fill="#0054AA">1</text></svg>
      <h3>Discovery Call</h3><p>We learn about your facility, your current systems, and where you are in the SQF journey. No pressure — just a conversation.</p>
    </div>
    <div class="step">
      <svg width="190" height="190" viewBox="0 0 190 190"><circle cx="95" cy="95" r="88" fill="none" stroke="#7BADD7" stroke-width="3" stroke-dasharray="330 6 2 6 2 6 2 6 2 6 2 6"/><circle cx="95" cy="95" r="72" fill="#7BADD7"/><circle cx="95" cy="95" r="55" fill="#fff"/><rect x="76" y="70" width="34" height="46" fill="none" stroke="#0054AA" stroke-width="3"/><path d="M83 82h20M83 92h14"/><circle cx="106" cy="108" r="9" fill="#fff" stroke="#0054AA" stroke-width="3"/><path d="M112 114l8 8" stroke="#0054AA" stroke-width="3"/><circle cx="27" cy="150" r="13" fill="#fff" stroke="#7BADD7" stroke-width="2"/><text x="27" y="155" text-anchor="middle" font-family="Lexend,sans-serif" font-size="14" fill="#0054AA">2</text></svg>
      <h3>Gap Assessment</h3><p>We evaluate your facility against SQF requirements, identify what's missing, and give you a clear roadmap with priorities.</p>
    </div>
    <div class="step">
      <svg width="190" height="190" viewBox="0 0 190 190"><circle cx="95" cy="95" r="88" fill="none" stroke="#7BADD7" stroke-width="3" stroke-dasharray="330 6 2 6 2 6 2 6 2 6 2 6"/><circle cx="95" cy="95" r="72" fill="#7BADD7"/><circle cx="95" cy="95" r="55" fill="#fff"/><circle cx="95" cy="95" r="14" fill="none" stroke="#0054AA" stroke-width="3"/><circle cx="95" cy="95" r="26" fill="none" stroke="#0054AA" stroke-width="3" stroke-dasharray="8 5"/><circle cx="27" cy="150" r="13" fill="#fff" stroke="#7BADD7" stroke-width="2"/><text x="27" y="155" text-anchor="middle" font-family="Lexend,sans-serif" font-size="14" fill="#0054AA">3</text></svg>
      <h3>Build &amp; Implement</h3><p>We design your SQF program and build it directly into your digital food safety platform — forms, logs, SOPs, HACCP plans, all of it.</p>
    </div>
    <div class="step">
      <svg width="190" height="190" viewBox="0 0 190 190"><circle cx="95" cy="95" r="88" fill="none" stroke="#7BADD7" stroke-width="3" stroke-dasharray="330 6 2 6 2 6 2 6 2 6 2 6"/><circle cx="95" cy="95" r="72" fill="#7BADD7"/><circle cx="95" cy="95" r="55" fill="#fff"/><rect x="74" y="72" width="42" height="30" fill="none" stroke="#0054AA" stroke-width="3"/><circle cx="95" cy="84" r="6" fill="none" stroke="#0054AA" stroke-width="3"/><path d="M70 116h50M86 102v14M104 102v14" stroke="#0054AA" stroke-width="3"/><circle cx="27" cy="150" r="13" fill="#fff" stroke="#7BADD7" stroke-width="2"/><text x="27" y="155" text-anchor="middle" font-family="Lexend,sans-serif" font-size="14" fill="#0054AA">4</text></svg>
      <h3>Coach &amp; Certify</h3><p>We train your team, run mock audits, and prepare you for certification day. Then we stay on as your ongoing SQF advisory partner.</p>
    </div>
  </div>
</section>

<section class="quote">
  <div class="quote-mark">”</div>
  <blockquote>"Northline Food Safety Group didn't just hand us a binder. They built our entire SQF system into software and coached our team until we owned it. We passed our first audit with confidence."</blockquote>
  <cite>— SQF-Certified Manufacturing Client</cite>
</section>

<section class="creds">
  <div class="cred"><svg width="36" height="40" viewBox="0 0 30 32" fill="none" stroke="#0054AA" stroke-width="2"><path d="M15 2l12 5v9c0 8-6 13-12 14C9 29 3 24 3 16V7z"/><path d="M10 16l4 4 7-8"/></svg>SQF Practitioner</div>
  <div class="cred"><span class="sigma">6σ</span>Six Sigma Black Belt</div>
  <div class="cred"><svg width="44" height="40" viewBox="0 0 44 40" fill="none" stroke="#0054AA" stroke-width="2"><circle cx="10" cy="10" r="5"/><circle cx="34" cy="10" r="5"/><circle cx="22" cy="28" r="6"/><path d="M14 13l5 10M30 13l-5 10"/></svg>Remote &amp; On-Site</div>
  <div class="cred"><svg width="44" height="40" viewBox="0 0 44 40" fill="none" stroke="#0054AA" stroke-width="2"><rect x="6" y="4" width="32" height="24"/><path d="M12 12h20M12 18h14M16 36h12M22 28v8"/></svg>Digital-First</div>
</section>

<section class="cta">
  <svg class="sec-icon" width="30" height="32" viewBox="0 0 30 32" fill="none" stroke="#ffffff" stroke-width="2"><path d="M15 2l12 5v9c0 8-6 13-12 14C9 29 3 24 3 16V7z"/><path d="M10 16l4 4 7-8"/></svg>
  <div class="sec-eyebrow">GET SQF CONSULTING</div>
  <h2>Ready to Talk SQF?</h2>
  <p>Share a few details about your facility and where you are in the SQF journey.<br>We'll follow up with a brief discovery call and a clear next step.</p>
  <div class="cta-actions"><a class="btn-white" href="#">Get My SQF Consultation ↗</a><a class="btn-ghost" href="#">Visit PlantInsightLab.io ↗</a></div>
</section>

<footer class="site-footer">
  <div class="foot-brand">
    <div class="brand"><span class="brand-mark"></span><div><div class="brand-name" style="font-size:19px">Northline Food Safety Group</div><div class="brand-sub">Food Safety &amp; SQF Certification</div></div></div>
    <p>Tech-driven SQF consulting for small and mid-size US food manufacturers. Based in Riverton, CA — serving clients across North America.</p>
  </div>
  <div class="foot-col" style="left:580px"><h5>SERVICES</h5><ul><li>SQF Program Design</li><li>Digital Platform Build</li><li>Coaching &amp; Support</li><li>Gap Assessments</li><li>Sanitation Programs</li></ul></div>
  <div class="foot-col contact" style="left:835px"><h5>CONNECT</h5><ul><li><span class="dot"></span>Email Us</li><li><span class="dot"></span>PlantInsightLab.io</li><li><span class="dot"></span>Professional Profile</li></ul></div>
  <div class="copyright">© 2026 Northline Food Safety Group LLC. All rights reserved. Created with Brightfield Studio</div>
</footer>

</body>
</html>
```